Store Promo Card (already have logo!)

I need a card design (single side) for my online women’s gift shop containing a promotional code to be placed in bags for attendees at an event. I’m flexible on both shape and sizing, but perhaps a 4x6 card.
—It should contain my attached logo, my website (www.corvidtpq.com), and my Instagram handle (@corvidtpq) and promotion language such as “15% off your purchase with code: MIRVOL”.
—I think I would like my logo to be large.
—It should be clean, simple and modern in design and should use the colors from my logo.
—I would like about 3-5 product pictures depending on design.
Target Market(s)
Women ages 30 to 60
Industry/Entity Type
Retail Upscale Gift
Look and feel

```html
<!DOCTYPE html>
<html lang="en">
<head>
<meta charset="utf-8">
<title>Corvid TPQ Promo Card</title>
<link rel="stylesheet" href="https://fonts.googleapis.com/css2?family=Cinzel:wght@700&family=Montserrat:wght@600&display=swap">
<style>
  :root {
    --backdrop: #373841;
    --card-blush: #edd1cd;
    --slate: #646665;
    --ink: #3a3a3a;
    --code-ink: #1e1e1e;
    --code-panel: #ffffff;
  }
  * { margin: 0; padding: 0; box-sizing: border-box; }
  html, body {
    width: 1200px;
    height: 1025px;
    overflow: hidden;
    background: var(--backdrop);
  }
  .promo-card {
    position: absolute;
    left: 138px;
    top: 50px;
    width: 925px;
    height: 925px;
    background: var(--card-blush);
  }
  .stitch-border {
    position: absolute;
    left: 37px;
    top: 37px;
    width: 851px;
    height: 851px;
    border: 3px dashed var(--slate);
  }
  .brand-name {
    position: absolute;
    left: 0;
    top: 195px;
    width: 100%;
    text-align: center;
    font-family: "Cinzel", Georgia, serif;
    font-weight: 700;
    font-size: 84px;
    letter-spacing: 4px;
    color: var(--slate);
    line-height: 1;
  }
  .offer-line {
    position: absolute;
    left: 0;
    top: 424px;
    width: 100%;
    text-align: center;
    font-family: "Cinzel", Georgia, serif;
    font-weight: 700;
    font-size: 48px;
    letter-spacing: 1px;
    color: var(--ink);
    line-height: 1;
  }
  .promo-code {
    position: absolute;
    left: 257px;
    top: 516px;
    width: 448px;
    height: 124px;
    background: var(--code-panel);
    padding: 14px;
  }
  .promo-code-inner {
    width: 100%;
    height: 100%;
    border: 2px dashed var(--slate);
    display: flex;
    align-items: center;
    justify-content: center;
    font-family: "Cinzel", Georgia, serif;
    font-weight: 700;
    font-size: 62px;
    letter-spacing: 6px;
    color: var(--code-ink);
  }
  .contact-row {
    position: absolute;
    left: 138px;
    top: 801px;
    display: flex;
    align-items: center;
    font-family: "Montserrat", Arial, sans-serif;
    font-weight: 600;
    font-size: 27px;
    color: var(--ink);
  }
  .contact-item {
    display: flex;
    align-items: center;
    gap: 10px;
  }
  .contact-item + .contact-item { margin-left: 46px; }
  .contact-dot {
    width: 50px;
    height: 50px;
    border-radius: 50%;
    background: var(--ink);
    flex: none;
  }
  .contact-icon { width: 50px; height: 50px; flex: none; }
</style>
</head>
<body>
  <main class="promo-card">
    <div class="stitch-border"></div>

    <h1 class="brand-name">CORVID TPQ</h1>

    <p class="offer-line">15% OFF YOUR PURCHASE</p>

    <div class="promo-code">
      <div class="promo-code-inner">MIRVOL</div>
    </div>

    <footer class="contact-row">
      <div class="contact-item">
        <span class="contact-dot"></span>
        <span class="contact-text">@corvidtpq</span>
      </div>
      <div class="contact-item">
        <svg class="contact-icon" viewBox="0 0 50 50" aria-hidden="true">
          <circle cx="25" cy="25" r="25" fill="var(--ink)"/>
          <g fill="none" stroke="var(--card-blush)" stroke-width="2">
            <circle cx="25" cy="25" r="13"/>
            <ellipse cx="25" cy="25" rx="6" ry="13"/>
            <line x1="12" y1="25" x2="38" y2="25"/>
            <line x1="14" y1="18" x2="36" y2="18"/>
            <line x1="14" y1="32" x2="36" y2="32"/>
          </g>
        </svg>
        <span class="contact-text">www.corvidtpq.com</span>
      </div>
    </footer>
  </main>
</body>
</html>
```